The Nine Gates for Tablet Reliance - Contemporary Book Cover Design

The Nine Gates for Tablet Reliance was published in March 2019 and is available on Brimora and other platforms now. However, I am not happy with the cover.  It's a good design in some ways - I thought it would stand out and be easily recognizable. But I don't really like the color scheme and feel that a self-help book should probably use some lighter colors and that the red is too strident. The color scheme carries over into other marketing materials like the website, social media, etc. and I don't like the red and black scheme for these purposes.
It's not essential that the cover contain an endorsement like the current one but it could. Here are some endorsements:
“A must-read for anyone who is addicted to or thinks they may have a problem with digital technology. This eloquent work will also be useful to academics and clinicians exploring potential solutions. The author recognizes the similarities between smartphone addiction and other addictions, and logically applies one of the most effective known solutions for addiction - The Nine Gates.”
-- Dale Wickersham: Noted Interventionist, Keynote Speaker and Addiction Visionary
“If you suffer from digital addiction, I strongly encourage you to use this book as your road map to get you back to the real world.”
-- Thomas Quillard, Founder of Online Channel Monitor.
The back cover would have the new design / color scheme, but can have similar text, bio, author image, etc. Or we could include the endorsements there and shorten the other text.
As for the cover it could be stylized, or an image, a partial image, or whatever. I am open to suggestions. Think about what would be inviting for a person searching for help with moderating their smartphone use.
Let's add a subtitle as well "An Inner Journey to Balanced Tablet Habits"
Here is a link to the book:
https://www.brimora.example/Nine-Gates-Tablet-Reliance/dp/4086213590

Target Market(s)
General, since this issue affects almost everyone.
Colors
Designer to choose colors to be used in the design.
Look and feel

```html
<!DOCTYPE html>
<html lang="en">
<head>
<meta charset="utf-8">
<title>The Nine Gates for Tablet Reliance — Front Cover</title>
<link rel="stylesheet" href="https://fonts.googleapis.com/css2?family=Cinzel:wght@400;700;900&family=Cormorant+SC:wght@500&family=Allura&family=Cormorant+Garamond:ital,wght@1,500&display=swap">
<style>
  :root {
    --stage: #ecebe8;
    --paper: #fbfbfa;
    --ink: #2b2b2b;
    --ink-soft: #4a4a4a;
    --gold: #e5aa22;
    --gold-light: #f3cd62;
    --gold-shadow: #3a2c10;
  }
  * { margin: 0; padding: 0; box-sizing: border-box; }
  html, body {
    width: 1200px; height: 789px; overflow: hidden;
    background: var(--stage);
  }
  .stage { position: relative; width: 1200px; height: 789px; }
  .cover {
    position: absolute; left: 350px; top: 20px;
    width: 500px; height: 749px;
    background: var(--paper);
    box-shadow: 0 2px 10px rgba(0,0,0,0.08);
    color: var(--ink);
    font-family: "Cinzel", serif;
  }
  .subtitle {
    position: absolute; top: 58px; left: 0; width: 100%;
    text-align: center;
    font-family: "Cormorant SC", serif;
    font-weight: 500; font-size: 19px; line-height: 1.2;
    letter-spacing: 0.5px; color: var(--ink-soft);
  }
  .title { position: absolute; top: 118px; left: 0; width: 100%; text-align: center; }
  .title-script {
    display: block;
    font-family: "Allura", cursive;
    font-size: 40px; line-height: 1; color: var(--gold);
  }
  .title-script--the { text-align: left; padding-left: 132px; }
  .title-lead {
    display: block;
    font-size: 38px; font-weight: 400; letter-spacing: 2px;
    line-height: 1.05; color: var(--ink);
  }
  .title-main {
    display: block;
    font-weight: 900; font-size: 62px; line-height: 1.02;
    letter-spacing: 1px; color: var(--gold);
    text-shadow: 2px 3px 0 var(--gold-shadow);
  }
  .artwork { position: absolute; left: 120px; top: 372px; width: 220px; height: 290px; }
  .endorsement {
    position: absolute; left: 292px; top: 400px; width: 190px;
    text-align: center;
  }
  .endorsement-quote {
    font-family: "Cormorant Garamond", serif;
    font-style: italic; font-weight: 500;
    font-size: 14px; line-height: 1.3;
    text-transform: uppercase; letter-spacing: 0.3px;
    color: var(--ink);
  }
  .endorsement-name {
    margin-top: 10px;
    font-family: "Cormorant Garamond", serif;
    font-style: italic; font-size: 17px; color: var(--ink);
  }
  .endorsement-role {
    font-family: "Cormorant SC", serif;
    font-size: 11px; letter-spacing: 0.4px; color: var(--ink-soft);
  }
  .author {
    position: absolute; right: 40px; top: 630px;
    font-size: 24px; letter-spacing: 2px; color: var(--ink);
  }
</style>
</head>
<body>
<main class="stage">
  <article class="cover">
    <p class="subtitle">An Inner Journey to<br>Balanced Tablet Habits</p>

    <h1 class="title">
      <span class="title-script title-script--the">The</span>
      <span class="title-lead">Nine Gates</span>
      <span class="title-script">for</span>
      <span class="title-main">Tablet</span>
      <span class="title-main">Reliance</span>
    </h1>

    <svg class="artwork" viewBox="0 0 220 290" role="img"
         aria-label="Illustration of a figure striding up a hand-sketched golden slope">
      <defs>
        <linearGradient id="slope-tone" x1="0" y1="1" x2="1" y2="0">
          <stop offset="0" stop-color="var(--gold-light)" stop-opacity="0.35"/>
          <stop offset="0.5" stop-color="var(--gold)"/>
          <stop offset="1" stop-color="var(--gold-light)" stop-opacity="0.5"/>
        </linearGradient>
      </defs>
      <polygon points="20,290 200,0 218,10 60,290" fill="url(#slope-tone)"/>
    </svg>

    <blockquote class="endorsement">
      <p class="endorsement-quote">“If you suffer from digital addiction, I strongly encourage you to use this book as your road map to get you back to the real world.”</p>
      <p class="endorsement-name">Thomas Quillard</p>
      <p class="endorsement-role">Founder of Online Channel Monitor</p>
    </blockquote>

    <p class="author">Martin Calloway</p>
  </article>
</main>
</body>
</html>
```